Orthodontic Postcard Design for Mailing to Potential Clients - This is a redesign of an existing one

I need to modify the attached "Back To School" ai file as follows:Front Side:* Back to school - change to - Grand Opening* Excellent orthodontic care... - change to - Excellent orthodontic care for your entire family. Increasing self-esteem by creating beautiful smiles is what we do!* See why so many of your neighbors.. - change to - See why so many of your neighbors are choosing Dr. Perlow for their family orthodontic needs.* Change address to - 4318 Camino Brisa Lenta, Suite 101Solmara, CA 92503(858) 720-1130* Change email address to -www.Braces.CareBack Side:*
Replace "Quality can be fun... with my quote "Classic smiles are what we do!" Dr. Perlow
Map (attached)
Eliminate current pictures - add girl with braces (attached) and my picture (attached)
Back to school... - replaced with a coupon that says Free Initial Orthodontic Consultation - Offer valid for sixty days.* Change address and websiteI would like to do these postcards every six weeks. Do you find the extra large cards more effective than the medium cards? What is the cost difference. I would like to send them to households in the 92503, 92587 and 92549 zip codes.

Target Market(s)

Typically age 7-16, and young adults

Industry/Entity Type

School

Requirements
Must have
• I need this project completed ASAP in order to send it to print.

```html
<!DOCTYPE html>
<html lang="en">
<head>
<meta charset="utf-8">
<title>Perlow Orthodontics Grand Opening Postcard</title>
<link rel="stylesheet" href="https://fonts.googleapis.com/css2?family=Arimo:wght@700&family=Crimson+Text:wght@400;600&family=Marcellus&family=Pinyon+Script&display=swap">
<style>
  :root {
    --red: #c8202c;
    --ink: #1c1a1a;
    --paper: #ffffff;
    --stage: #e9e7e4;
    --highlight: #f4ef5a;
    --photo-warm: #d9a77a;
    --photo-cool: #8ea3bf;
    --photo-suit: #4a4442;
    --map-tone: #ecebe8;
  }
  * { box-sizing: border-box; margin: 0; padding: 0; }
  html, body { width: 1200px; height: 1000px; overflow: hidden; }
  body { background: var(--stage); position: relative; font-family: "Crimson Text", serif; color: var(--ink); }

  .card { position: absolute; width: 822px; height: 449px; background: var(--paper); box-shadow: 0 2px 6px rgba(0,0,0,.18); overflow: hidden; }
  .card--front { left: 42px; top: 38px; }
  .card--back { left: 330px; top: 513px; }
  .abs { position: absolute; }
  .sans-bold { font-family: "Arimo", sans-serif; font-weight: 700; }

  /* Wordmark: one font, one weight, one colour */
  .wordmark { font-family: "Marcellus", serif; font-weight: 400; color: var(--red); line-height: 1; white-space: nowrap; }
  .wordmark__name { display: block; font-size: 64px; }
  .wordmark__trade { display: block; font-size: 29px; margin-top: 2px; padding-left: 78px; }

  /* Front */
  .photo-girl { left: 0; top: 0; width: 191px; height: 305px; background: linear-gradient(160deg, #e2c27c 0%, var(--photo-warm) 55%, #d25a6e 100%); }
  .photo-boy { left: 688px; top: 167px; width: 134px; height: 222px; background: linear-gradient(180deg, #b58c62 0%, var(--photo-cool) 45%, #5d7190 85%, #f2f2f2 100%); border-radius: 40px 40px 8px 8px; }
  .headline { left: 230px; top: 30px; width: 440px; text-align: center; font-family: "Marcellus", serif; font-weight: 400; color: var(--ink); line-height: 1; }
  .headline__l1 { font-size: 46px; display: block; }
  .headline__l2 { font-size: 44px; display: block; margin-top: 4px; }
  .headline__l2 small { font-size: 34px; }
  .headline__l3 { display: block; margin-top: 2px; white-space: nowrap; }
  .headline__script { font-family: "Pinyon Script", cursive; color: var(--red); font-size: 72px; }
  .headline__smile { font-size: 56px; }
  .intro { left: 240px; top: 212px; width: 440px; text-align: center; font-size: 17px; line-height: 1.15; }
  .band { left: 338px; top: 286px; width: 484px; height: 38px; background: linear-gradient(90deg, rgba(200,32,44,0) 0%, var(--red) 45%, var(--red) 100%); }
  .burst { left: 632px; top: 0; width: 190px; height: 150px; }
  .burst__text { left: 700px; top: 26px; width: 110px; text-align: center; color: var(--paper); }
  .burst__title { font-size: 17px; line-height: 1; display: block; }
  .burst__sub { font-size: 13px; line-height: 1.05; display: block; margin-top: 2px; }
  .brand-front { left: 16px; top: 322px; }
  .neighbors { left: 316px; top: 336px; width: 390px; font-size: 15.5px; line-height: 1.25; text-align: center; }
  .neighbors span { background: linear-gradient(180deg, transparent 45%, var(--highlight) 45%, var(--highlight) 85%, transparent 85%); }
  .address { left: 321px; top: 384px; font-size: 12.5px; line-height: 1.2; }
  .address .phone { font-size: 14px; }
  .web { left: 620px; top: 390px; width: 170px; text-align: center; color: var(--red); font-size: 18px; line-height: 1.1; }

  /* Back */
  .panel { left: 0; top: 0; width: 488px; height: 285px; background: var(--red); }
  .photo-doctor { left: 13px; top: 17px; width: 150px; height: 197px; border: 2px solid var(--paper); background: linear-gradient(180deg, #f0ede6 0%, #e5c6a8 35%, var(--photo-suit) 70%, #2f2b2a 100%); }
  .map { left: 175px; top: 15px; width: 302px; height: 199px; background: var(--map-tone); border: 2px solid var(--paper); }
  .map__info { left: 356px; top: 122px; width: 116px; font-size: 10.5px; line-height: 1.15; }
  .map__brand { display: block; font-family: "Marcellus", serif; color: var(--red); font-size: 13px; line-height: 1.1; margin-bottom: 3px; white-space: nowrap; }
  .map__info .phone { color: var(--red); font-size: 13px; }
  .quote { left: 15px; top: 221px; width: 150px; color: var(--paper); font-size: 16.5px; line-height: 1.15; }
  .quote__by { display: block; text-align: right; font-style: italic; }
  .located { left: 175px; top: 221px; width: 300px; text-align: center; color: var(--paper); font-size: 16.5px; line-height: 1.2; }
  .faq { left: 500px; top: 17px; width: 310px; height: 156px; border: 5px solid var(--red); padding: 10px 14px; }
  .faq__q { color: var(--red); font-size: 16.5px; line-height: 1.1; }
  .faq__a { font-size: 15.5px; line-height: 1.1; margin-top: 4px; width: 212px; }
  .faq__age { right: 10px; top: 48px; color: var(--red); font-size: 96px; line-height: 1; letter-spacing: -4px; }
  .brand-back { left: 16px; top: 318px; }
  .coupon { left: 281px; top: 312px; width: 208px; height: 112px; border: 4px solid var(--red); padding: 8px 10px; color: var(--ink); }
  .coupon__main { font-size: 21px; line-height: 1.1; }
  .coupon__main em { color: var(--red); font-style: normal; }
  .coupon__terms { font-size: 12.5px; margin-top: 4px; }
</style>
</head>
<body>
  <section class="card card--front" aria-label="Postcard front">
    <div class="abs photo-girl" role="img" aria-label="Photo of a smiling teenage girl with braces"></div>
    <svg class="abs burst" viewBox="0 0 190 150" aria-hidden="true">
      <polygon fill="#c8202c" points="130,72 190,60 140,84 190,100 138,94 176,140 128,102 130,150 118,106 96,150 110,98 60,130 104,86 40,96 102,76 40,40 110,66 90,0 120,60 140,0 132,64 185,10 138,70"/>
      <circle cx="122" cy="72" r="56" fill="#c8202c"/>
    </svg>
    <div class="abs burst__text">
      <span class="burst__title sans-bold">GRAND OPENING!</span>
      <span class="burst__sub">Now accepting new patients.</span>
    </div>
    <h1 class="abs headline">
      <span class="headline__l1">Brace</span>
      <span class="headline__l2">Yourself <small>for a</small></span>
      <span class="headline__l3"><span class="headline__script">Classic</span><span class="headline__smile">Smile!</span></span>
    </h1>
    <p class="abs intro">Excellent orthodontic care for your entire family.<br>Increasing self-esteem by creating<br>beautiful smiles is what we do!</p>
    <div class="abs band"></div>
    <div class="abs photo-boy" role="img" aria-label="Photo of a teenage boy sitting with his arms around his knees"></div>
    <div class="abs wordmark brand-front"><span class="wordmark__name">Perlow</span><span class="wordmark__trade">Orthodontics</span></div>
    <p class="abs neighbors"><span>See why so many of your neighbors are choosing</span><br><span>Dr. Perlow for their family orthodontic needs.</span></p>
    <p class="abs address">4318 Camino Brisa Lenta • Suite 101<br>Solmara, CA 92503<br><span class="phone">(858) 463-0297</span></p>
    <p class="abs web">visit us at<br>www.Tooveli.Care</p>
  </section>

  <section class="card card--back" aria-label="Postcard back">
    <div class="abs panel"></div>
    <div class="abs photo-doctor" role="img" aria-label="Portrait photo of Dr. Perlow in a suit"></div>
    <div class="abs map" role="img" aria-label="Street map showing the office location near the freeway"></div>
    <p class="abs map__info"><span class="map__brand">Perlow Orthodontics</span>4318 Camino Brisa Lenta<br>Suite 101<br>Solmara, CA 92503<br><span class="phone">(858) 463-0297</span></p>
    <p class="abs quote sans-bold">"Classic smiles are what we do!"<span class="quote__by">Dr. Perlow</span></p>
    <p class="abs located sans-bold">Located in the Harborline<br>Savings Building</p>
    <div class="abs faq">
      <p class="faq__q sans-bold">At what age should my child see an orthodontist?</p>
      <p class="faq__a">The National Orthodontic Council recommends that children be seen for an initial consultation at age</p>
      <span class="abs faq__age sans-bold">7.</span>
    </div>
    <div class="abs wordmark brand-back"><span class="wordmark__name">Perlow</span><span class="wordmark__trade">Orthodontics</span></div>
    <div class="abs coupon sans-bold">
      <p class="coupon__main"><em>FREE</em> Initial Orthodontic Consultation</p>
      <p class="coupon__terms">Offer valid for sixty days.</p>
    </div>
  </section>
</body>
</html>
```